Financial Coaching biz needs modern service presentation menu

We need a PowerPoint presentation document with a modern, easy-to-read layout to share with potential clients.

I have a website under development that can be used as a reference www.brightledgerhub.com.

We'd like the doc to be simple to edit because services and verbiage will likely be modified periodically.

Two logo variations have been included.

Target Market(s)

Gen X, Gen Y, and Millienials

Industry/Entity Type

Financial Planning

Colors
85cae6
cadf82
ffffff
dddddd
cfcfcf
cee9f5

```html
<!DOCTYPE html>
<html lang="en">
<head>
<meta charset="utf-8">
<title>BrightLedger Hub – Service Menu</title>
<link rel="stylesheet" href="https://fonts.googleapis.com/css2?family=Open+Sans:wght@400;600;700;800&family=Oswald:wght@400;500&display=swap">
<style>
:root{
  --page:#ececec;
  --white:#ffffff;
  --panel:#d6d6d6;
  --panel-dark:#585858;
  --cell-dark:#5a5a5a;
  --col-grey:#7b7b7b;
  --col-grey-dark:#6a6a6a;
  --blue:#1e9ad6;
  --green:#2bb673;
  --olive:#8b9c1c;
  --orange:#e8920d;
  --rust:#d9540b;
  --brand:#2bb673;
  --mascot-tone:#dcdcdc;
  --text-light:#f2f2f2;
}
*{box-sizing:border-box;margin:0;padding:0}
html,body{width:1200px;height:936px;overflow:hidden;background:var(--page)}
body{position:relative;font-family:"Open Sans",Arial,sans-serif}

.slide{position:absolute;width:572px;height:404px;background:var(--panel);overflow:hidden}
.slide--services{left:30px;top:52px}
.slide--compare{left:611px;top:52px;width:573px}
.slide--benefits{left:30px;top:471px;width:570px;height:403px}
.slide--promise{left:611px;top:470px;width:573px;background:var(--white)}

.slide__header{position:absolute;left:0;top:0;right:0;height:82px;background:var(--white)}
.brand{position:absolute;left:34px;top:24px;display:flex;align-items:center;gap:10px}
.brand__dot{width:34px;height:34px;border-radius:50%;background:var(--panel)}
.brand__name{font-weight:800;font-size:24px;line-height:1;color:var(--brand);letter-spacing:.5px;width:150px}
.mascot-decor{position:absolute;right:0;top:0;width:205px;height:82px;background:linear-gradient(90deg,var(--white),var(--mascot-tone))}

/* service columns */
.service-row{position:absolute;left:16px;top:112px;display:flex;gap:7px}
.service{width:103px;height:268px;position:relative}
.service__tab{position:absolute;left:0;right:0;top:0;height:60px;border-radius:26px 26px 0 0}
.service__icon{position:absolute;left:50%;top:0;width:52px;height:52px;margin-left:-26px;border-radius:50%;background:var(--white);display:flex;align-items:center;justify-content:center}
.service__title{position:absolute;left:0;right:0;top:52px;height:52px;display:flex;align-items:center;justify-content:center;text-align:center;color:var(--white);font-weight:700;font-size:11px;line-height:1.1;letter-spacing:.3px}
.service__body{position:absolute;left:0;right:0;top:104px;height:150px;background:var(--col-grey);color:var(--text-light);font-size:7.2px;line-height:1.5;text-align:center;padding:8px 4px}
.service__body p+p{margin-top:9px}
.service__body--large{font-size:9.4px;line-height:1.35;padding:10px 6px}
.service:nth-child(even) .service__body{background:var(--col-grey-dark)}
.service__foot{position:absolute;left:0;right:0;top:254px;height:14px}
.floor{position:absolute;left:0;right:0;top:378px;height:4px;background:linear-gradient(#9a9a9a,transparent)}

.c-blue .service__tab,.c-blue .service__title,.c-blue .service__foot{background:var(--blue)}
.c-green .service__tab,.c-green .service__title,.c-green .service__foot{background:var(--green)}
.c-olive .service__tab,.c-olive .service__title,.c-olive .service__foot{background:var(--olive)}
.c-orange .service__tab,.c-orange .service__title,.c-orange .service__foot{background:var(--orange)}
.c-rust .service__tab,.c-rust .service__title,.c-rust .service__foot{background:var(--rust)}

/* comparison table */
.compare{position:absolute;left:15px;top:106px;display:grid;grid-template-columns:127px 67px 62px 88px 88px 108px;grid-template-rows:44px repeat(7,30px);gap:2px}
.compare__head{background:var(--blue);color:var(--white);font-weight:700;font-size:11.5px;line-height:1.2;display:flex;align-items:center;justify-content:center;text-align:center;letter-spacing:.4px}
.compare__head--first{border-top-left-radius:6px}
.compare__head--last{border-top-right-radius:6px}
.compare__blank{background:transparent}
.compare__label,.compare__cell{display:flex;align-items:center;justify-content:center;color:var(--white)}
.compare__label{font-weight:700;font-size:9.6px;line-height:1.15;text-align:center;letter-spacing:.4px}
.row-dark{background:var(--cell-dark)}
.row-green{background:var(--green)}
.tick{width:20px;height:20px}

/* benefits */
.benefit-row{position:absolute;left:28px;top:97px;display:flex;gap:6px}
.benefit{width:126px;height:262px;position:relative}
.benefit__tab{position:absolute;left:0;right:0;top:0;height:90px;border-radius:46px 46px 0 0}
.benefit__icon{position:absolute;left:50%;top:8px;width:70px;height:70px;margin-left:-35px;border-radius:50%;background:var(--white);display:flex;align-items:center;justify-content:center}
.benefit__title{position:absolute;left:0;right:0;top:86px;height:44px;background:var(--col-grey);color:var(--white);font-family:"Oswald",Arial,sans-serif;font-size:13px;line-height:1.3;text-align:center;display:flex;align-items:center;justify-content:center;letter-spacing:.3px}
.benefit__body{position:absolute;left:0;right:0;top:130px;height:132px;color:var(--white);font-weight:700;font-size:7.5px;line-height:1.48;text-align:center;padding:6px 7px}
.benefit__body p+p{margin-top:7px}
.b-green .benefit__tab,.b-green .benefit__body{background:var(--green)}
.b-blue .benefit__tab,.b-blue .benefit__body{background:var(--blue)}
.b-orange .benefit__tab,.b-orange .benefit__body{background:var(--orange)}
.b-olive .benefit__tab,.b-olive .benefit__body{background:var(--olive)}
.benefit-floor{position:absolute;left:0;right:0;top:359px;height:4px;background:linear-gradient(#9a9a9a,transparent)}
.benefits-caption{position:absolute;left:0;right:0;top:363px;text-align:center;font-family:"Oswald",Arial,sans-serif;font-weight:500;font-size:19px;letter-spacing:1px;color:var(--panel-dark)}
.vip{font-family:"Oswald",Arial,sans-serif;font-weight:500;font-size:28px;color:var(--olive);letter-spacing:1px}

/* promise */
.promise{position:absolute;left:0;right:0;top:104px;height:270px;background:var(--panel-dark)}
.stripe{position:absolute;height:6px}
.stripe--top-green{left:0;width:462px;top:6px;background:var(--green)}
.stripe--top-blue{left:462px;right:0;top:6px;background:var(--blue)}
.stripe--bottom-blue{left:0;width:110px;top:252px;background:var(--blue)}
.stripe--bottom-green{left:110px;right:0;top:252px;background:var(--green)}
.guarantee-seal{position:absolute;left:36px;top:58px;width:140px;height:128px;border-radius:50%;border:8px solid var(--white)}
.promise__text{position:absolute;left:205px;width:348px;top:38px;color:var(--white);font-weight:700;font-size:9.6px;line-height:1.28;text-align:center}
.promise__text p+p{margin-top:12px}
</style>
</head>
<body>

<!-- Slide: services overview -->
<section class="slide slide--services">
  <header class="slide__header">
    <div class="brand"><span class="brand__dot"></span><span class="brand__name">BRIGHTLEDGER HUB</span></div>
    <div class="mascot-decor" role="img" aria-label="Faint enlarged mascot wearing green glasses"></div>
  </header>
  <div class="service-row">
    <article class="service c-blue">
      <div class="service__tab"></div>
      <div class="service__icon"><svg width="30" height="30" viewBox="0 0 30 30" fill="none" stroke="#1e9ad6" stroke-width="2"><rect x="3" y="4" width="24" height="16"/><path d="M8 16v-3M13 16v-6M18 16v-4M23 16V8M15 20v7M10 27l5-7 5 7"/></svg></div>
      <h3 class="service__title">MONETARY<br>ACTION PLAN</h3>
      <div class="service__body service__body--large"><p>Establish full-year plan for spending and saving, including major purchases or events</p></div>
      <div class="service__foot"></div>
    </article>
    <article class="service c-green">
      <div class="service__tab"></div>
      <div class="service__icon"><svg width="30" height="30" viewBox="0 0 30 30" fill="none" stroke="#2bb673" stroke-width="2"><rect x="3" y="5" width="22" height="20"/><path d="M3 11h22M8 3v4M20 3v4M7 15h3M12 15h3M17 15h3M7 20h3M12 20h3"/><rect x="19" y="18" width="9" height="10" fill="#fff"/></svg></div>
      <h3 class="service__title">BUDGETING<br>SERVICE</h3>
      <div class="service__body"><p>Unlimited consultations to determine holes and waste in spending</p><p>Client choice from multiple budgeting strategies to determine best personal fit</p></div>
      <div class="service__foot"></div>
    </article>
    <article class="service c-olive">
      <div class="service__tab"></div>
      <div class="service__icon"><svg width="30" height="30" viewBox="0 0 30 30"><rect x="3" y="7" width="24" height="16" rx="2" fill="#8b9c1c"/><rect x="3" y="11" width="24" height="3" fill="#fff"/><rect x="6" y="17" width="8" height="2" fill="#fff"/></svg></div>
      <h3 class="service__title">BRIGHTLEDGER'S<br>CREDIT-ED<br>SERVICE</h3>
      <div class="service__body"><p>Personalized assessment with ALL 3 bureaus</p><p>All Documentation provided for future use and personal records</p><p>Provide tools, knowledge, and strategy to prevent future missteps</p></div>
      <div class="service__foot"></div>
    </article>
    <article class="service c-orange">
      <div class="service__tab"></div>
      <div class="service__icon"><svg width="30" height="30" viewBox="0 0 30 30" fill="#e8920d"><circle cx="11" cy="9" r="4"/><path d="M5 26v-8a6 6 0 0 1 12 0v8z"/><circle cx="21" cy="13" r="3"/><path d="M17 26v-6a4 4 0 0 1 8 0v6z"/></svg></div>
      <h3 class="service__title">ASSET<br>ADVOCATE</h3>
      <div class="service__body"><p>Complimentary Rental and Mortgage Assessment</p><p>Quarterly Insurance Assessment</p><p>Quarterly Utility Assessment</p></div>
      <div class="service__foot"></div>
    </article>
    <article class="service c-rust">
      <div class="service__tab"></div>
      <div class="service__icon"><svg width="30" height="30" viewBox="0 0 30 30"><rect x="7" y="3" width="16" height="24" fill="#d9540b"/><path d="M10 10h10M10 14h10M10 18h10M10 22h6" stroke="#fff" stroke-width="1.5"/></svg></div>
      <h3 class="service__title">TAX<br>PREPARATION</h3>
      <div class="service__body"><p>Free prior year return review and amendment filing</p><p>Guarantee best price</p><p>Partnership discount applied with all future filings</p></div>
      <div class="service__foot"></div>
    </article>
  </div>
  <div class="floor"></div>
</section>

<!-- Slide: comparison table -->
<section class="slide slide--compare">
  <header class="slide__header">
    <div class="brand"><span class="brand__dot"></span><span class="brand__name">BRIGHTLEDGER HUB</span></div>
    <div class="mascot-decor" role="img" aria-label="Faint enlarged mascot wearing green glasses"></div>
  </header>
  <svg width="0" height="0" style="position:absolute">
    <symbol id="tick" viewBox="0 0 24 24"><path d="M19 9.5A8 8 0 1 1 15 4.6" fill="none" stroke="#fff" stroke-width="2.6" stroke-linecap="round"/><path d="M7.5 11.5l4 4L21 5" fill="none" stroke="#fff" stroke-width="2.8" stroke-linecap="round" stroke-linejoin="round"/></symbol>
  </svg>
  <div class="compare">
    <div class="compare__blank"></div>
    <div class="compare__head compare__head--first">TAXPOINT</div>
    <div class="compare__head">FILE<br>FAST</div>
    <div class="compare__head">COINCOURSE</div>
    <div class="compare__head">CREDITLEX</div>
    <div class="compare__head compare__head--last">BRIGHTLEDGER<br>HUB</div>

    <div class="compare__label row-dark">TAX PREPARATION</div>
    <div class="compare__cell row-dark"><svg class="tick"><use href="#tick"/></svg></div>
    <div class="compare__cell row-dark"><svg class="tick"><use href="#tick"/></svg></div>
    <div class="compare__cell row-dark"></div><div class="compare__cell row-dark"></div>
    <div class="compare__cell row-dark"><svg class="tick"><use href="#tick"/></svg></div>

    <div class="compare__label row-green">CREDIT<br>EDUCATION</div>
    <div class="compare__cell row-green"></div><div class="compare__cell row-green"></div><div class="compare__cell row-green"></div>
    <div class="compare__cell row-green"><svg class="tick"><use href="#tick"/></svg></div>
    <div class="compare__cell row-green"><svg class="tick"><use href="#tick"/></svg></div>

    <div class="compare__label row-dark">BUDEGTING<br>SERVICE</div>
    <div class="compare__cell row-dark"></div><div class="compare__cell row-dark"></div>
    <div class="compare__cell row-dark"><svg class="tick"><use href="#tick"/></svg></div>
    <div class="compare__cell row-dark"></div>
    <div class="compare__cell row-dark"><svg class="tick"><use href="#tick"/></svg></div>

    <div class="compare__label row-green">ASSET ADVOCACY</div>
    <div class="compare__cell row-green"></div><div class="compare__cell row-green"></div><div class="compare__cell row-green"></div><div class="compare__cell row-green"></div>
    <div class="compare__cell row-green"><svg class="tick"><use href="#tick"/></svg></div>

    <div class="compare__label row-dark">MONETARY<br>ACTION PLAN</div>
    <div class="compare__cell row-dark"></div><div class="compare__cell row-dark"></div><div class="compare__cell row-dark"></div><div class="compare__cell row-dark"></div>
    <div class="compare__cell row-dark"><svg class="tick"><use href="#tick"/></svg></div>

    <div class="compare__label row-green">SAVING BUILDER</div>
    <div class="compare__cell row-green"></div><div class="compare__cell row-green"></div><div class="compare__cell row-green"></div><div class="compare__cell row-green"></div>
    <div class="compare__cell row-green"><svg class="tick"><use href="#tick"/></svg></div>

    <div class="compare__label row-dark">IN-PERSON FACE<br>TO FACE SERVICE</div>
    <div class="compare__cell row-dark"><svg class="tick"><use href="#tick"/></svg></div>
    <div class="compare__cell row-dark"></div><div class="compare__cell row-dark"></div><div class="compare__cell row-dark"></div>
    <div class="compare__cell row-dark"><svg class="tick"><use href="#tick"/></svg></div>
  </div>
</section>

<!-- Slide: partnership benefits -->
<section class="slide slide--benefits">
  <header class="slide__header">
    <div class="brand"><span class="brand__dot"></span><span class="brand__name">BRIGHTLEDGER HUB</span></div>
    <div class="mascot-decor" role="img" aria-label="Faint enlarged mascot wearing green glasses"></div>
  </header>
  <div class="benefit-row">
    <article class="benefit b-green">
      <div class="benefit__tab"></div>
      <div class="benefit__icon"><svg width="40" height="40" viewBox="0 0 40 40"><circle cx="20" cy="20" r="15" fill="#2bb673"/><text x="20" y="27" text-anchor="middle" font-family="Open Sans,Arial,sans-serif" font-weight="700" font-size="20" fill="#fff">$</text></svg></div>
      <h3 class="benefit__title">SAVINGS BUILDER</h3>
      <div class="benefit__body"><p>Tired of the banks not paying interest? Want to put money away but you're afraid you don't have enough to start with.</p><p>Well we pay a CASH BONUS for staying on track with your savings goal, no matter how small the amount</p></div>
    </article>
    <article class="benefit b-blue">
      <div class="benefit__tab"></div>
      <div class="benefit__icon" role="img" aria-label="Mascot holding a calculator"><svg width="44" height="44" viewBox="0 0 44 44"><circle cx="22" cy="22" r="20" fill="#1e9ad6"/></svg></div>
      <h3 class="benefit__title">IN-PERSON BUDGET<br>BEAR SERVICE</h3>
      <div class="benefit__body"><p>You get a professional negotiator at the table with you for major purchases.</p><p>You can also take your strategist with you to the mall or grocer to help you stay on budget</p></div>
    </article>
    <article class="benefit b-orange">
      <div class="benefit__tab"></div>
      <div class="benefit__icon"><svg width="44" height="40" viewBox="0 0 44 40" fill="none" stroke="#e8920d" stroke-width="4" stroke-linecap="round"><circle cx="13" cy="7" r="4" fill="#e8920d" stroke="none"/><circle cx="31" cy="7" r="4" fill="#e8920d" stroke="none"/><path d="M4 15h36M13 14v10M31 14v10M13 24l-5 12M13 24l5 12M31 24l-5 12M31 24l5 12"/></svg></div>
      <h3 class="benefit__title">COUPON COMPANION</h3>
      <div class="benefit__body"><p>Don't have time or feel like clipping coupons, we have an EXTREME COUPONER on staff to notify clients when great deals come up</p></div>
    </article>
    <article class="benefit b-olive">
      <div class="benefit__tab"></div>
      <div class="benefit__icon"><span class="vip">VIP</span></div>
      <h3 class="benefit__title">VIP SEMINAR ACCESS</h3>
      <div class="benefit__body"><p>Learn about credit, home buying, budgeting, taxes, negotiating, refinancing loans, starting a business, and more in an intimate, small group setting</p></div>
    </article>
  </div>
  <div class="benefit-floor"></div>
  <p class="benefits-caption">SPECIAL BENEFITS FOR FULL PARTNERSHIP</p>
</section>

<!-- Slide: our promise -->
<section class="slide slide--promise">
  <header class="slide__header">
    <div class="brand"><span class="brand__dot"></span><span class="brand__name">BRIGHTLEDGER HUB</span></div>
    <div class="mascot-decor" role="img" aria-label="Faint enlarged mascot wearing green glasses"></div>
  </header>
  <div class="promise">
    <span class="stripe stripe--top-green"></span><span class="stripe stripe--top-blue"></span>
    <div class="guarantee-seal" role="img" aria-label="Satisfaction guarantee seal"></div>
    <div class="promise__text">
      <p>We provide a FREE CONSULTATION and conduct a full assessment before we take on any new client. Therefore, prospective clients find out upfront if we can actually help them.</p>
      <p>We pride ourselves on being good corporate citizens as well. For every new household we sign, we commit to providing free service to household below the poverty line.</p>
      <p>Our promise is that we won't take on or charge a client a single cent unless we are ABSOLUTELY SURE we can add value.</p>
      <p>Our company is fundamentally built upon the service and the help we provide.<br>So if we can't help you, we won't charge you. PERIOD.</p>
    </div>
    <span class="stripe stripe--bottom-blue"></span><span class="stripe stripe--bottom-green"></span>
  </div>
</section>

</body>
</html>
```